Presentation Folder - Stagger Cut Fliers
Keystone Realty Group
Presentation Folder - Stagger Cut Fliers - Real Estate
Creative Brief
Real Estate
Corporate. Our target audience are real estate agents and brokers. This is an industry where image and perception matter, so these designs need to invoke professionalism, be creative, and invoke confidence in our services.
The presentation folder itself needs to be very simple, but again, very professional and aesthetically pleasing. At a minimum, we need our logo on the font and the company contact information on the back. The stagger cut fliers themselves need to have the ability to put information on the front and back of the flier. There are five pages for the fliers, so you can either design five unique pages or have a template that can work for all of them. You can use filler text like that in the attached document. The fliers aren't just going to be text. You can add filler images to make more appealing, such as on the consumer demand page you can leave a spot where we can put the image of a billboard.

```html
<!DOCTYPE html>
<html lang="en">
<head>
<meta charset="utf-8">
<title>Keystone Realty Group – Presentation Folder</title>
<link rel="stylesheet" href="https://fonts.googleapis.com/css2?family=Open+Sans:wght@400;600&display=swap">
<style>
  :root {
    --backdrop: #8c8c8c;
    --paper: #ffffff;
    --paper-shade: #eef0f2;
    --ink: #3a3d42;
    --ink-soft: #5c6066;
    --brand-blue: #1b8fd6;
    --pocket-light: #27a9e6;
    --pocket-dark: #0b6bb4;
  }
  * { margin: 0; padding: 0; box-sizing: border-box; }
  html, body { width: 1200px; height: 1080px; overflow: hidden; }
  body {
    background: var(--backdrop);
    font-family: "Open Sans", Arial, sans-serif;
    color: var(--ink);
    position: relative;
  }
  .folder {
    position: absolute;
    left: 55px; top: 50px;
    width: 1090px; height: 980px;
    box-shadow: 0 6px 18px rgba(0,0,0,0.35);
    overflow: hidden;
  }
  .folder-inside {
    position: absolute; inset: 0;
    background:
      radial-gradient(ellipse at 50% 60%, var(--paper-shade) 0%, var(--paper) 55%),
      var(--paper);
  }
  .folder-inside::after {
    content: "";
    position: absolute; left: 545px; top: 0; bottom: 0; width: 1px;
    background: rgba(0,0,0,0.06);
  }
  .pockets { position: absolute; left: 0; top: 725px; width: 1090px; height: 255px; }

  .brand { display: flex; align-items: center; position: absolute; }
  .brand-dot { border-radius: 50%; background: var(--brand-blue); flex: none; }
  .brand-name { font-weight: 600; color: var(--ink); line-height: 1; white-space: nowrap; }

  .brand-cover { left: 655px; top: 305px; gap: 14px; }
  .brand-cover .brand-dot { width: 62px; height: 62px; }
  .brand-cover .brand-name { font-size: 30px; }

  .brand-back { left: 40px; top: 630px; gap: 10px; }
  .brand-back .brand-dot { width: 34px; height: 34px; }
  .brand-back .brand-name { font-size: 16px; }

  .contact {
    position: absolute; left: 285px; top: 622px;
    font-size: 10.5px; line-height: 1.45; color: var(--ink-soft);
  }
  .contact .row { display: flex; gap: 14px; }
  .contact .label { width: 46px; }
  .contact .address { margin-bottom: 6px; }

  .website {
    position: absolute; left: 845px; top: 698px;
    font-size: 11px; color: var(--ink-soft);
  }
</style>
</head>
<body>
  <div class="folder">
    <div class="folder-inside"></div>

    <div class="brand brand-back">
      <span class="brand-dot"></span>
      <span class="brand-name">Keystone Realty Group</span>
    </div>
    <div class="contact">
      <div class="address">1840 Harbor Crest Dr., Ste. B<br>Ridgeview, Texas 77412</div>
      <div class="row"><span class="label">Toll free</span><span>(800) 555-0142</span></div>
      <div class="row"><span class="label">Phone</span><span>(555) 555-0187</span></div>
      <div class="row"><span class="label">Fax</span><span>(555) 555-0163</span></div>
    </div>

    <div class="brand brand-cover">
      <span class="brand-dot"></span>
      <span class="brand-name">Keystone Realty Group</span>
    </div>
    <div class="website">www.KeystoneRealtyGroup.com</div>

    <svg class="pockets" viewBox="0 0 1090 255" preserveAspectRatio="none" aria-hidden="true">
      <defs>
        <linearGradient id="pocketFill" x1="0" y1="0" x2="0" y2="1">
          <stop offset="0" stop-color="#27a9e6"/>
          <stop offset="1" stop-color="#0b6bb4"/>
        </linearGradient>
        <linearGradient id="pocketSheen" x1="0" y1="0" x2="1" y2="0">
          <stop offset="0" stop-color="#0b6bb4" stop-opacity="0.45"/>
          <stop offset="0.5" stop-color="#ffffff" stop-opacity="0"/>
          <stop offset="1" stop-color="#0b6bb4" stop-opacity="0.45"/>
        </linearGradient>
      </defs>
      <polygon points="0,0 520,0 545,255 0,255" fill="url(#pocketFill)"/>
      <polygon points="0,0 520,0 545,255 0,255" fill="url(#pocketSheen)"/>
      <polygon points="572,10 1090,10 1090,255 545,255" fill="url(#pocketFill)"/>
      <polygon points="572,10 1090,10 1090,255 545,255" fill="url(#pocketSheen)"/>
    </svg>
  </div>
</body>
</html>
```